Business Card Design for boarding house accomodation business

I need a business card design for my Sydney based boarding house business accomodation. providing rooms for rent in Sydney Australia with shard bathroom and kitchen.
The front of card, are my details with details of head office and the rear of card to have details of locations providing rooms for rent.

Industry/Entity Type

Business

Contact Information for Business Card

Front of card details:
HOLLINBROOK MANAGEMENT PTY LTD t/a
CALLOWAY'S GUEST HOUSE
ABN:52930718264
Daniel Vukasinov
48 Pembury st
Newtown 2042
Mobile:0412876390
Email:daniel@callowaysguesthouse-example.com.au

Back of Card:
Locations:
-48 Pembury st
Newtown 2042

-392 Carvel st
Erskineville 2043

-87 Whitlam st
Bondi 2026

-264 Ashcombe rd
Marrickville 2043

```html
<!DOCTYPE html>
<html lang="en">
<head>
<meta charset="utf-8">
<title>Calloway's Guest House – Business Cards</title>
<link rel="stylesheet" href="https://fonts.googleapis.com/css2?family=Open+Sans:wght@400;600;700;800&family=Roboto+Condensed:wght@400;700&display=swap">
<style>
  :root {
    --page-bg: #e9e9e6;
    --card-white: #ffffff;
    --grey-light: #c9cacc;
    --grey-mid: #a9abae;
    --grey-dark: #6f7175;
    --blue-deep: #0f4f92;
    --blue-mid: #1f73b7;
    --blue-light: #2f9bd0;
    --green: #5cb82e;
    --green-dark: #3e9a24;
    --green-light: #8fd13f;
    --ink: #2b2b2b;
    --ink-soft: #555;
  }
  * { box-sizing: border-box; margin: 0; padding: 0; }
  html, body { width: 1200px; height: 913px; overflow: hidden; }
  body {
    background: var(--page-bg);
    font-family: "Open Sans", Arial, sans-serif;
    color: var(--ink);
    position: relative;
  }
  .card {
    position: absolute;
    left: 250px;
    width: 700px;
    height: 390px;
    background: var(--card-white);
    box-shadow: 0 6px 18px rgba(0,0,0,.18);
    overflow: hidden;
  }
  .card--back { top: 37px; }
  .card--front { top: 486px; }
  .card__art { position: absolute; inset: 0; width: 100%; height: 100%; }

  /* back card */
  .back-brand {
    position: absolute;
    left: 40px;
    top: 120px;
    font-weight: 800;
    font-size: 28px;
    line-height: 1.15;
    color: var(--card-white);
    letter-spacing: .5px;
  }
  .location {
    position: absolute;
    font-family: "Roboto Condensed", Arial, sans-serif;
    font-size: 15px;
    line-height: 1.3;
    color: var(--ink);
    padding-left: 12px;
    border-left: 5px solid var(--green);
  }
  .location--1 { left: 40px;  top: 296px; }
  .location--2 { left: 205px; top: 262px; }
  .location--3 { left: 375px; top: 228px; }
  .location--4 { left: 545px; top: 194px; }

  /* front card */
  .front-brand {
    position: absolute;
    right: 40px;
    top: 34px;
    text-align: right;
    color: var(--card-white);
  }
  .front-brand__entity {
    font-size: 15px;
    font-weight: 400;
    letter-spacing: .6px;
  }
  .front-brand__name {
    font-size: 24px;
    font-weight: 800;
    letter-spacing: .4px;
    margin-top: 2px;
  }
  .owner-details {
    position: absolute;
    left: 468px;
    top: 178px;
    font-size: 14px;
    line-height: 1.35;
    color: var(--ink-soft);
    padding-left: 12px;
    border-left: 5px solid var(--green);
  }
  .owner-details__name { font-weight: 700; color: var(--ink); }
  .contact-phone {
    position: absolute;
    left: 40px;
    top: 292px;
    display: flex;
    align-items: center;
    gap: 14px;
    font-size: 31px;
    font-weight: 700;
    color: var(--blue-mid);
    letter-spacing: .5px;
  }
  .contact-email {
    position: absolute;
    left: 40px;
    top: 345px;
    display: flex;
    align-items: center;
    gap: 10px;
    font-size: 12px;
    color: var(--ink-soft);
  }
  .icon { display: block; flex: none; }
</style>
</head>
<body>

  <!-- Back of card: locations -->
  <section class="card card--back" aria-label="Back of card – locations">
    <svg class="card__art" viewBox="0 0 700 390" aria-hidden="true">
      <defs>
        <linearGradient id="greyFacets" x1="0" y1="0" x2="1" y2="1">
          <stop offset="0" stop-color="var(--grey-mid)"/>
          <stop offset=".55" stop-color="var(--grey-light)"/>
          <stop offset="1" stop-color="var(--grey-dark)"/>
        </linearGradient>
        <linearGradient id="greenBandBack" x1="0" y1="0" x2="1" y2="0">
          <stop offset="0" stop-color="var(--green-light)"/>
          <stop offset="1" stop-color="var(--green-dark)"/>
        </linearGradient>
      </defs>
      <polygon points="0,0 700,0 700,140 440,165 0,262" fill="url(#greyFacets)" role="img" aria-label="Faceted grey geometric background"/>
      <polygon points="0,262 440,165 700,140 700,162 470,182 0,270" fill="var(--green)"/>
      <polygon points="0,368 700,368 700,390 0,390" fill="url(#greenBandBack)"/>
    </svg>
    <div class="back-brand">CALLOWAY'S<br>GUEST HOUSE</div>
    <p class="location location--1">48 Pembury st,<br>Newtown, 2042.</p>
    <p class="location location--2">392 Carvel st,<br>Erskineville, 2043.</p>
    <p class="location location--3">87 Whitlam st,<br>Bondi, 2026.</p>
    <p class="location location--4">264 Ashcombe rd,<br>Marrickville, 2043.</p>
  </section>

  <!-- Front of card: owner details -->
  <section class="card card--front" aria-label="Front of card – contact details">
    <svg class="card__art" viewBox="0 0 700 390" aria-hidden="true">
      <defs>
        <linearGradient id="blueFacets" x1="0" y1="1" x2="1" y2="0">
          <stop offset="0" stop-color="var(--blue-deep)"/>
          <stop offset=".6" stop-color="var(--blue-mid)"/>
          <stop offset="1" stop-color="var(--blue-light)"/>
        </linearGradient>
        <linearGradient id="greenBandFront" x1="0" y1="0" x2="1" y2="0">
          <stop offset="0" stop-color="var(--green-light)"/>
          <stop offset="1" stop-color="var(--green-dark)"/>
        </linearGradient>
      </defs>
      <polygon points="0,0 700,0 700,112 430,160 0,262" fill="url(#blueFacets)" role="img" aria-label="Faceted blue geometric background"/>
      <polygon points="0,262 430,160 700,112 700,132 455,176 0,270" fill="var(--green)"/>
      <polygon points="0,368 700,368 700,390 0,390" fill="url(#greenBandFront)"/>
    </svg>

    <div class="front-brand">
      <p class="front-brand__entity">HOLLINBROOK MANAGEMENT PTY LTD t/a</p>
      <p class="front-brand__name">CALLOWAY'S GUEST HOUSE</p>
    </div>

    <div class="owner-details">
      <p>ABN: 52930718264</p>
      <p class="owner-details__name">Daniel Vukasinov</p>
      <p>48 Pembury st,</p>
      <p>Newtown, 2042.</p>
    </div>

    <p class="contact-phone">
      <svg class="icon" width="30" height="30" viewBox="0 0 30 30" aria-hidden="true">
        <circle cx="15" cy="15" r="13" fill="none" stroke="var(--blue-mid)" stroke-width="2.5"/>
        <path d="M10.5 8.5c1-.6 1.8-.3 2.3.6l1 2c.3.7.1 1.3-.4 1.7l-.8.6c.6 1.6 1.8 2.9 3.4 3.6l.7-.8c.5-.5 1.1-.6 1.7-.3l2 1.1c.8.5 1 1.3.5 2.2-.8 1.4-2.2 1.9-3.7 1.3-3.6-1.4-6.2-4.1-7.4-7.6-.5-1.6.1-3.3.7-4.4z" fill="var(--blue-mid)"/>
      </svg>
      0412876390
    </p>

    <p class="contact-email">
      <svg class="icon" width="16" height="16" viewBox="0 0 16 16" aria-hidden="true">
        <circle cx="8" cy="8" r="8" fill="var(--ink)"/>
        <rect x="4" y="5" width="8" height="6" rx="1" fill="none" stroke="#fff" stroke-width="1.2"/>
        <path d="M4.3 5.4 8 8.3l3.7-2.9" fill="none" stroke="#fff" stroke-width="1.2"/>
      </svg>
      daniel@callowaysguesthouse-example.com.au
    </p>
  </section>

</body>
</html>
```